New Modern floristry business design

Hi, we are a new business based in Sydney called "velvet moss floristry"

With so many floristry's we need a good design that will set a great first impression.

A few descriptive words on how we envision velvet moss floristry:

-dynamic design
-minimal colour (colour can be used to enhance the design)
-black white grey (can include gold,silver,metallic shadowing)
Strong "VELVET MOSS" with a classy "FLORISTRY"
Bold with a touch of feminine

Industry/Entity Type

Business

Contact Information for Business Card

Velvet Moss Floristry,
Delphine Ruvek,
Velvetmossfloristry@quillmail.com.au

```html
<!DOCTYPE html>
<html lang="en">
<head>
<meta charset="utf-8">
<title>Velvet Moss Floristry – Business Card</title>
<link rel="stylesheet" href="https://fonts.googleapis.com/css2?family=Cormorant+Garamond:ital,wght@1,500&family=Great+Vibes&family=Russo+One&display=swap">
<style>
  :root {
    --bg-warm: #f7d990;
    --bg-mid: #e3dcbc;
    --bg-cool: #c6d5d6;
    --brand-steel: #6f7273;
    --brand-gold: #b8860b;
    --ink: #111111;
    --bouquet-light: #f4f7ea;
    --bouquet-mid: #b9cf9c;
    --bouquet-dark: #2f4a2c;
  }
  html, body {
    margin: 0;
    padding: 0;
    overflow: hidden;
  }
  .card {
    position: relative;
    width: 1200px;
    height: 741px;
    overflow: hidden;
    background: linear-gradient(120deg, var(--bg-warm) 0%, var(--bg-mid) 50%, var(--bg-cool) 100%);
  }
  .brand-name {
    position: absolute;
    left: 196px;
    top: 88px;
    width: 770px;
    margin: 0;
    font-family: "Russo One", "Arial Black", sans-serif;
    font-weight: 400;
    font-size: 104px;
    line-height: 1.1;
    letter-spacing: 1px;
    color: var(--brand-steel);
    text-align: center;
    white-space: nowrap;
  }
  .brand-tagline {
    position: absolute;
    left: 528px;
    top: 226px;
    margin: 0;
    font-family: "Great Vibes", "Brush Script MT", cursive;
    font-weight: 400;
    font-size: 168px;
    line-height: 1.2;
    color: var(--brand-gold);
    white-space: nowrap;
  }
  .bouquet {
    position: absolute;
    left: 113px;
    top: 232px;
    width: 395px;
    height: 252px;
    border-radius: 48% 52% 55% 45% / 50% 45% 55% 50%;
    background: radial-gradient(ellipse at 55% 40%, var(--bouquet-light) 0%, var(--bouquet-mid) 45%, var(--bouquet-dark) 100%);
  }
  .contact {
    position: absolute;
    left: 254px;
    top: 498px;
    margin: 0;
    font-family: "Cormorant Garamond", Georgia, serif;
    font-style: italic;
    font-weight: 500;
    font-size: 53px;
    line-height: 76px;
    color: var(--ink);
    white-space: nowrap;
  }
  .contact span {
    display: block;
  }
</style>
</head>
<body>
  <div class="card">
    <h1 class="brand-name">Velvet Moss</h1>
    <div class="bouquet" role="img" aria-label="Photograph of a white bouquet of roses and calla lilies with baby's breath and green leaves"></div>
    <p class="brand-tagline">Floristry</p>
    <p class="contact">
      <span class="contact-name">Velvet Moss Floristry, Delphine Ruvek</span>
      <span class="contact-email">Velvetmossfloristry@quillmail.com.au</span>
    </p>
  </div>
</body>
</html>
```